Book Cover Design Project

I have written a booK called "keep the lamp Lit:
a guide to starting and running a small business. It is aimed at the start up entrepreneur and seeks to give them everything they need to start up and run a small business. I am interested in a very simple cover that is contemporary in the look but clearly communicates the mission of the book. It should sell very well as there are no others like it, so the designer will get excellent exposure.
Updates

Reason: I an vacation in Europe until the 23rd of July. Would like a few days to make a decision after my return Walt

We are currently on vacation.  Will make a final decision in about a week.  Thanks so much for your submissions

Walt

Target Market(s)

Start up businesses in the U.S.

Industry/Entity Type

Business

Requirements
Must have
• Clear communication of the name. Lots of white space. Graphic communication of the purpose of the book? Prominent exposure of my name. Walter j. Pennick

```html
<!DOCTYPE html>
<html lang="en">
<head>
<meta charset="utf-8">
<title>Keep the Lamp Lit – Book Cover</title>
<link rel="stylesheet" href="https://fonts.googleapis.com/css2?family=Cinzel:wght@400;500&display=swap">
<style>
  :root {
    --backdrop: #141414;
    --paper: #ffffff;
    --ink: #2b2724;
    --accent: #f08a1c;
    --accent-text: #ffffff;
    --compass-light: #d9c9a3;
    --compass-mid: #a88a5c;
    --compass-dark: #5a3d22;
  }
  html, body {
    margin: 0;
    padding: 0;
    width: 1200px;
    height: 900px;
    overflow: hidden;
    background: var(--backdrop);
  }
  .canvas {
    position: relative;
    width: 1200px;
    height: 900px;
  }
  .book-cover {
    position: absolute;
    left: 336px;
    top: 40px;
    width: 528px;
    height: 820px;
    background: var(--paper);
    font-family: "Cinzel", "Trajan Pro", serif;
    color: var(--ink);
    text-align: center;
  }
  .title {
    position: absolute;
    left: 0;
    right: 0;
    top: 22px;
    margin: 0;
    font-weight: 400;
  }
  .title-main {
    display: block;
    font-size: 150px;
    line-height: 1;
    letter-spacing: 2px;
  }
  .title-rest {
    display: block;
    margin-top: 6px;
    font-size: 54px;
    line-height: 1;
    letter-spacing: 2px;
  }
  .cover-emblem {
    position: absolute;
    left: 150px;
    top: 320px;
    width: 228px;
    height: 260px;
  }
  .subtitle {
    position: absolute;
    left: 0;
    right: 0;
    top: 556px;
    margin: 0;
    font-size: 37px;
    font-weight: 400;
    line-height: 58px;
    letter-spacing: 0.5px;
  }
  .author-band {
    position: absolute;
    left: 0;
    right: 0;
    bottom: 0;
    height: 50px;
    background: var(--accent);
    color: var(--accent-text);
    font-size: 27px;
    line-height: 52px;
    letter-spacing: 0.5px;
  }
</style>
</head>
<body>
<div class="canvas">
  <article class="book-cover">
    <h1 class="title">
      <span class="title-main">KEEP</span>
      <span class="title-rest">THE LAMP LIT</span>
    </h1>

    <svg class="cover-emblem" viewBox="0 0 228 260" role="img" aria-label="Antique brass compass with its needle pointing to success">
      <defs>
        <radialGradient id="emblem-fill" cx="50%" cy="45%" r="55%">
          <stop offset="0%" stop-color="var(--compass-light)"/>
          <stop offset="70%" stop-color="var(--compass-mid)"/>
          <stop offset="100%" stop-color="var(--compass-dark)"/>
        </radialGradient>
        <radialGradient id="emblem-shadow" cx="50%" cy="50%" r="50%">
          <stop offset="0%" stop-color="#000" stop-opacity="0.25"/>
          <stop offset="100%" stop-color="#000" stop-opacity="0"/>
        </radialGradient>
      </defs>
      <ellipse cx="114" cy="238" rx="100" ry="12" fill="url(#emblem-shadow)"/>
      <circle cx="114" cy="120" r="114" fill="url(#emblem-fill)"/>
    </svg>

    <h2 class="subtitle">
      A GUIDE TO<br>
      STARTING AND RUNNING<br>
      A SMALL BUSINESS
    </h2>

    <div class="author-band">AUTHOR NAME</div>
  </article>
</div>
</body>
</html>
```